author needs a Book Cover design

Needs a book cover design that matches the title in some way.
Book Title is- 9 Lanterns Beneath a Quiet Harbor Tonight.
Subtile- Harvest Lessons Across Ordinary Seasons.
Author Name:-Desmond Okorefe, Jr.

Final Design is subject to Book Publisher's requirement.

Font styles to use
Serif

Requirements
Must have
• Follow these recommended specifications for your cover file:
• Page Size: Your cover should be a single (one-piece) PDF that includes the back cover, spine, and front cover. You can submit your cover on any size page as long as the printable area is measured exactly for your book's trim size, spine width, and allows at least .125” bleed, centered horizontally and vertically.
• Minimum Cover Width: Bleed + Back Cover Trim Size + Spine Width + Front Cover Trim Size + Bleed
• Minimum Cover Height: Bleed + Book Height Trim Size + Bleed
• Trim Size: Your cover should be the same trim size as you choose in the Title Information when setting up your book. For example, submitting a cover that was previously used for a 6.25” x 9.25” book would not work for a 6” x 9” book.
• Barcodes: For manufacturing and distribution reasons, your book's back cover must include a valid ISBN barcode. If your cover already has an ISBN barcode, make sure it is high-resolution, or at least 300 dpi, and 1.5" - 2" in width with proportional height. Ideally, this barcode should be 2” wide by 1.2” tall. Also, check to make sure you have the rights to use the ISBN on your cover, because not all services allow you to use their ISBNs elsewhere.
• QR codes: There are no set size restrictions, but the quality (resolution) of the image must be set to at least 300 dpi. Make sure you have the rights to use the code.
• If your artwork does not include a barcode, we will automatically add one in the lower right-hand corner of your book's back cover, free of charge. Our system will place the ISBN barcode in a space 2" wide and 1.2" tall. The bottom of this barcode is located 1/4" up from the bottom trim line of the cover. The right side of the barcode is located 1/4" to the left of the spine. Please ensure that you don't have any important images or text in the barcode location. You can also refer to our Artwork Templates for the exact size and position of the ISBN barcode on your final cover.
• If you don’t have an ISBN already on your cover, but you have live graphic or text elements in the location that our system will place the ISBN, you will need to move those elements or place the ISBN in a different location yourself.
• Publishing Logos: We do not add our logo to your book.
• Spine Width and Variance: If your artwork was created for a different service, please make sure that the spine width of your current cover matches our spine width. Different services may use different paper thickness, which is why the spine width of your cover artwork could be correct for another service but incorrect for our service.
• Ideally, you should avoid hard vertical lines separating your front or back cover panels from your spine and should allow for at least a .125" variance of your spine on each side (for example, the text on a 1" spine should be no larger than .75" wide). For books with a page count of less than 130 pages, we strongly recommend a blank spine.
• Your spine width should be calculated based on the number of pages in your book and using the appropriate formula:
• Black and White Interior Book Spine Width:
• White paper: Number of pages x .002252 = Spine width in inches
• Cream paper: Number of pages x .0025 = Spine width in inches
• Color Interior Book Spine Width:
• Number of pages x .002347 = Spine width in inches
• Example of spine width calculation for a 120-page black and white interior book with white paper:
• 120 x .002252 = .27" spine width
• Text and Image Placement: All live cover elements, or text and images that cannot be cut, must be at least .125" inside the trim lines to ensure no important elements are cut during the bookmaking process and the appearance of your printed books is consistent.
• Bleed: Your cover's background must extend at least .125" beyond the final trim line to accommodate for cutting/trimming tolerance.
• Crop/Registration Marks: Please do not include any crop or registration marks on your files, as they may interfere with the binding process or appear on the cover. We use our own measurements, specific to our systems, for cutting and binding; crop or registration marks placed by you could interfere with this process.
• Images and Fonts: Any images you include on your book's cover may be tagged with your choice of CMYK or RGB profiles or left untagged in a generic color space. All images should be sized at 100%, flattened to one layer and placed in your native document at a resolution of at least 300 DPI. You should also embed all fonts in your PDF file.
• Desmond, I hope this information is helpful to you. Please feel free to contact us if you have any other questions or concerns.
• Best regards,
• *WILL SUPPLY THE PAGE NUMBERS INFORMATION
• Lisbeth
• PrintHollow Member Services
Nice to have
• An attractive design that matches the title. Design can include backgrounds

```html
<!DOCTYPE html>
<html lang="en">
<head>
<meta charset="utf-8">
<title>9 Lanterns Beneath a Quiet Harbor Tonight — Full Cover</title>
<link rel="stylesheet" href="https://fonts.googleapis.com/css2?family=Cinzel:wght@600;700&family=Cinzel+Decorative:wght@700;900&family=Oswald:wght@500&display=swap">
<style>
  :root {
    --ink: #000000;
    --gold: #c7852a;
    --gold-bright: #f6d23a;
    --gold-deep: #a86a12;
    --band: #9c6418;
    --band-light: #e8d3a8;
    --band-text: #1a1208;
    --wood-dark: #2a1608;
    --wood-mid: #6b3c17;
    --wood-glow: #c98a3c;
    --photo: #b45ad6;
  }
  html, body { margin: 0; padding: 0; overflow: hidden; background: var(--ink); }
  .cover {
    position: relative; width: 1200px; height: 900px; overflow: hidden;
    background: var(--ink); font-family: "Cinzel", serif;
  }
  /* back cover */
  .back-blurb, .back-bio {
    position: absolute; color: var(--gold); font-weight: 700;
    font-size: 12px; line-height: 19px; letter-spacing: 0.2px;
    text-align: justify; margin: 0;
  }
  .back-blurb { left: 46px; top: 56px; width: 472px; }
  .back-divider {
    position: absolute; left: 268px; top: 338px; width: 136px; height: 34px;
    background: radial-gradient(ellipse at 50% 50%, var(--gold-deep) 0%, rgba(168,106,18,.45) 40%, rgba(0,0,0,0) 72%);
  }
  .author-photo {
    position: absolute; left: 46px; top: 394px; width: 164px; height: 164px;
    background: radial-gradient(circle at 50% 55%, #d8c8b8 0%, #9a7a66 35%, var(--photo) 70%);
  }
  .back-bio { left: 46px; top: 386px; width: 478px; line-height: 19.4px; }
  .back-bio .wrap-space { float: left; width: 178px; height: 184px; }
  /* spine */
  .spine-title {
    position: absolute; left: 600px; top: 450px; width: 500px;
    transform: translate(-50%, -50%) rotate(-90deg);
    text-align: center; font-family: "Cinzel", serif; font-weight: 700;
    color: var(--gold-bright); font-size: 34px; line-height: 33px;
  }
  /* front cover */
  .front-art {
    position: absolute; left: 680px; top: 190px; width: 488px; height: 566px;
    background:
      radial-gradient(ellipse at 52% 62%, #f2c067 0%, var(--wood-glow) 18%, var(--wood-mid) 45%, var(--wood-dark) 80%, var(--ink) 100%);
  }
  .front-title {
    position: absolute; left: 680px; top: 30px; width: 488px; margin: 0;
    text-align: center; font-family: "Cinzel Decorative", serif; font-weight: 900;
    font-size: 50px; line-height: 58px; color: var(--gold-bright);
    text-shadow: 2px 3px 0 var(--gold-deep), 0 0 10px rgba(0,0,0,.8);
  }
  .front-title span { display: block; }
  .front-subtitle {
    position: absolute; left: 680px; top: 778px; width: 488px; margin: 0;
    text-align: center; color: var(--gold); font-weight: 700; font-size: 19px;
    letter-spacing: 0.4px; white-space: nowrap;
  }
  .author-band {
    position: absolute; left: 0; top: 828px; width: 1200px; height: 72px;
    background: var(--band); border-top: 4px solid var(--band-light);
    box-sizing: border-box;
  }
  .author-name {
    position: absolute; right: 68px; top: 8px; margin: 0;
    font-family: "Oswald", sans-serif; font-weight: 500; font-size: 38px;
    color: var(--band-text); letter-spacing: 0.5px;
  }
</style>
</head>
<body>
<div class="cover">

  <p class="back-blurb">Abundant Life is experienced as one hears and then puts into practice the Word of God. Jesus emphasized this point that the blessing is in the doing (practice). Jesus said, “But even more blessed are all who hear the word of God and put it into practice” (Luke 11:28 Plain Path Rendering). Also, He said, “Now that you know these things, God will bless you for doing them” (John 13:17 PPR).<br>The point of this book therefore, is to encourage the believer to adopt these Old Testament truths for daily living by making practical everyday decisions to walk in these covenant realities. For the believer to realize the Abundant Life (John 10:10), he must be a practitioner. Practicing the Word of God is a proven covenant technique for victorious living. I believe you are on your way to living Abundantly and fulfilling your covenant destiny.<br>Dr. Desmond Okorefe, Jr.</p>

  <div class="back-divider" role="img" aria-label="Decorative gold flourish divider"></div>

  <div class="author-photo" role="img" aria-label="Portrait photo of the author in a light suit against a violet background"></div>

  <p class="back-bio"><span class="wrap-space"></span>Desmond O. Okorefe, Jr. Ph.D., is Senior Pastor of the Stillwater Bible Fellowship Church, Alder Ridge, Marlowe County. A visionary and a missionary, he has traveled extensively, preaching and lecturing in several countries, and has studied and demonstrated proficiency in various fields such as Theology, Education, Christian Counseling, Writing, Speaking and Applied Sciences, (Biochemistry, Bacteriology Public Health). Dr. Okorefe is author of online daily devotions, ‘Morning Wellspring’, and President of RISE-BROTHERS+, an International Ministry to Men. He is president of Stillwater International Christian Ministries and Protestant Minister, for the Marlowe County Department of Restoration and is an ordained Bishop with the FGFA Ministries, (Fellowship of Gospel Faith Assemblies). He is blessed with his wife Pastor Imara and their four children.</p>

  <div class="spine-title">9 Lanterns Beneath a<br>Quiet Harbor Tonight</div>

  <div class="front-art" role="img" aria-label="Photo of a lit candle on an open Bible between two open hands, before a weathered wooden wall"></div>

  <h1 class="front-title"><span>9 Lanterns</span><span>Beneath a</span><span>Quiet Harbor</span><span>Tonight</span></h1>

  <p class="front-subtitle">Harvest Lessons Across Ordinary Seasons</p>

  <div class="author-band">
    <p class="author-name">DESMOND OKOREFE, JR.</p>
  </div>

</div>
</body>
</html>
```